Simple elegant business card

General card for a fin and television director.
Just want name, email, phone and address.

Target Market(s)

Prospective employers

Industry/Entity Type

Business

Requirements
Must have
• As above
Nice to have
• Logo but not necessary.
Should not have
• Not too colourful or funky.
• Simplicity and elegance the way to go.

```html
<!DOCTYPE html>
<html lang="en">
<head>
<meta charset="utf-8">
<title>Nora Hale – Business Card</title>
<link rel="stylesheet" href="https://fonts.googleapis.com/css2?family=Inter:wght@300;400&display=swap">
<style>
  :root {
    --page-bg: #d9dadc;
    --card-bg: #060708;
    --card-text: #f4f4f4;
  }
  * { margin: 0; padding: 0; box-sizing: border-box; }
  html, body {
    width: 1200px;
    height: 733px;
    overflow: hidden;
    background: var(--page-bg);
  }
  .stage {
    position: relative;
    width: 1200px;
    height: 733px;
  }
  .business-card {
    position: absolute;
    left: 50px;
    top: 61px;
    width: 1100px;
    height: 611px;
    background: var(--card-bg);
  }
  .contact-block {
    position: absolute;
    left: 652px;
    top: 284px;
    color: var(--card-text);
    font-family: "Inter", sans-serif;
    font-weight: 300;
    list-style: none;
  }
  .contact-name {
    font-size: 49px;
    line-height: 60px;
    letter-spacing: 0.5px;
    font-weight: 300;
  }
  .contact-line {
    font-size: 38px;
    line-height: 46.5px;
  }
</style>
</head>
<body>
  <main class="stage">
    <section class="business-card" aria-label="Business card of Nora Hale">
      <address class="contact-block" style="font-style: normal;">
        <h1 class="contact-name">NORA HALE</h1>
        <p class="contact-line">norahale@mail.com</p>
        <p class="contact-line">+1 310 555 0142</p>
        <p class="contact-line">218 Harbor Lane</p>
        <p class="contact-line">Bayview</p>
        <p class="contact-line">90017 CA USA</p>
      </address>
    </section>
  </main>
</body>
</html>
```